Need Help having my business card stand out

I am the owner of Pine Ridge Canine Coaching and would like for my business cards to stand out. I have been trying to keep designing them myself but I can't get what I have in my head on the card. I will try my best to post templates that I like for inspirations. I want something unique but elegant. I don't want in to look cartoony or cheesy. It needs to pop in a pet shop but also in a coffee shop or gym.

Target Market(s)

Dog owners, Married ,No young kids Jr High school kids and up (maybe kids on the way) Executives, Stay at home moms/wives, Small business owners

Industry/Entity Type

Dog Training

Contact Information for Business Card

Trevor Holloway, 555-304-7162, info@pineridgecanine.example, www.pineridgecanine.example

Colors

Designer to choose colors to be used in the design.

Requirements
Must have
• my logo
Should not have
• Cursive lettering

```html
<!DOCTYPE html>
<html lang="en">
<head>
<meta charset="utf-8">
<title>Pine Ridge Canine Coaching – Business Card</title>
<link rel="stylesheet" href="https://fonts.googleapis.com/css2?family=Oswald:wght@400;600&display=swap">
<style>
  :root {
    --board: #e6e6e6;
    --card: #ffffff;
    --ink: #111111;
    --band-grey: #8c8c8c;
    --text-grey: #6e6e6e;
    --icon-grey: #c9c9c9;
    --photo-light: #d9d9d9;
    --photo-mid: #9a9a9a;
    --photo-dark: #5c5c5c;
  }
  html, body {
    margin: 0;
    padding: 0;
    width: 1200px;
    height: 1200px;
    overflow: hidden;
    background: var(--board);
  }
  .board {
    position: relative;
    width: 1200px;
    height: 1200px;
    font-family: "Oswald", sans-serif;
  }
  .card {
    position: absolute;
    width: 439px;
    height: 725px;
    background: var(--card);
    box-shadow: 8px 8px 10px rgba(0,0,0,0.35);
    overflow: hidden;
  }
  .card-front { left: 139px; top: 145px; }
  .card-back  { left: 622px; top: 270px; }

  .card-bands { position: absolute; inset: 0; }

  .brand-name {
    position: absolute;
    left: 40px;
    top: 185px;
    width: 310px;
    text-align: center;
    font-weight: 600;
    color: var(--ink);
    text-transform: uppercase;
    line-height: 1.05;
  }
  .brand-name .line-1 { display: block; font-size: 54px; letter-spacing: 2px; }
  .brand-name .line-2 { display: block; font-size: 34px; letter-spacing: 1px; }

  .contact-row {
    position: absolute;
    display: flex;
    align-items: center;
    color: var(--text-grey);
    font-weight: 400;
    white-space: nowrap;
  }
  .contact-row svg { position: absolute; }
  .contact-name  { left: 104px; top: 446px; font-size: 31px; letter-spacing: 4px; }
  .contact-phone { left: 119px; top: 500px; font-size: 26px; letter-spacing: 6px; }
  .contact-email { left: 134px; top: 556px; font-size: 20px; letter-spacing: 1px; }
  .contact-web   { left: 149px; top: 606px; font-size: 20px; letter-spacing: 1px; }

  .icon { position: absolute; width: 26px; height: 26px; }
  .icon-person { left: 41px;  top: 451px; }
  .icon-phone  { left: 54px;  top: 504px; }
  .icon-mail   { left: 71px;  top: 556px; }
  .icon-globe  { left: 84px;  top: 606px; }

  .photo {
    position: absolute;
    inset: 0;
    background: linear-gradient(170deg, var(--photo-light) 0%, var(--photo-mid) 45%, var(--photo-dark) 100%);
  }
  .back-badge {
    position: absolute;
    left: 28px;
    top: 266px;
    width: 188px;
    height: 188px;
    border-radius: 50%;
    background: rgba(255,255,255,0.45);
  }
  .back-brand {
    position: absolute;
    left: 36px;
    top: 318px;
    width: 180px;
    font-weight: 600;
    color: var(--ink);
    text-transform: uppercase;
    line-height: 1.05;
    text-align: center;
  }
  .back-brand .line-1 { display: block; font-size: 31px; }
  .back-brand .line-2 { display: block; font-size: 20px; }

  .standalone-brand {
    position: absolute;
    left: 78px;
    top: 1010px;
    font-weight: 600;
    color: var(--ink);
    text-transform: uppercase;
    line-height: 1.05;
    text-align: center;
  }
  .standalone-brand .line-1 { display: block; font-size: 38px; letter-spacing: 1px; }
  .standalone-brand .line-2 { display: block; font-size: 24px; }
</style>
</head>
<body>
<main class="board">

  <section class="card card-front" aria-label="Business card front">
    <svg class="card-bands" width="439" height="725" viewBox="0 0 439 725" aria-hidden="true">
      <polygon points="311,0 439,0 439,395" fill="var(--band-grey)"/>
      <polygon points="335,0 439,0 439,330" fill="var(--ink)"/>
      <polygon points="0,203 155,725 0,725" fill="var(--band-grey)"/>
      <polygon points="0,268 130,725 0,725" fill="var(--ink)"/>
    </svg>

    <div class="brand-name">
      <span class="line-1">Pine Ridge</span>
      <span class="line-2">Canine Coaching</span>
    </div>

    <svg class="icon icon-person" viewBox="0 0 24 24" aria-hidden="true">
      <circle cx="12" cy="8" r="5" fill="var(--icon-grey)"/>
      <path d="M2 22c0-6 4.5-8.5 10-8.5S22 16 22 22z" fill="var(--icon-grey)"/>
    </svg>
    <svg class="icon icon-phone" viewBox="0 0 24 24" aria-hidden="true">
      <path d="M6 3l3 4-2 2c1 3 4 6 7 7l2-2 4 3-2 4C10 21 3 14 2 5z" fill="none" stroke="var(--icon-grey)" stroke-width="1.8" stroke-linejoin="round"/>
      <path d="M15 3a6 6 0 0 1 6 6M15 7a2 2 0 0 1 2 2" fill="none" stroke="var(--icon-grey)" stroke-width="1.6"/>
    </svg>
    <svg class="icon icon-mail" viewBox="0 0 24 24" aria-hidden="true">
      <rect x="2" y="5" width="20" height="14" fill="none" stroke="var(--icon-grey)" stroke-width="1.8"/>
      <path d="M2 5l10 8 10-8M2 19l7-7M22 19l-7-7" fill="none" stroke="var(--icon-grey)" stroke-width="1.6"/>
    </svg>
    <svg class="icon icon-globe" viewBox="0 0 24 24" aria-hidden="true">
      <circle cx="12" cy="12" r="10" fill="var(--icon-grey)"/>
      <path d="M2 12h20M12 2v20M4 7h16M4 17h16" stroke="var(--ink)" stroke-width="1.2" fill="none"/>
      <ellipse cx="12" cy="12" rx="4.5" ry="10" fill="none" stroke="var(--ink)" stroke-width="1.2"/>
    </svg>

    <div class="contact-row contact-name">TREVOR HOLLOWAY</div>
    <div class="contact-row contact-phone">555-304-7162</div>
    <div class="contact-row contact-email">INFO@PINERIDGECANINE.EXAMPLE</div>
    <div class="contact-row contact-web">WWW.PINERIDGECANINE.EXAMPLE</div>
  </section>

  <section class="card card-back" aria-label="Business card back">
    <div class="photo" role="img" aria-label="Black and white photo of the trainer kneeling on grass beside a shepherd dog in a park"></div>
    <div class="back-badge" aria-hidden="true"></div>
    <div class="back-brand">
      <span class="line-1">Pine Ridge</span>
      <span class="line-2">Canine Coaching</span>
    </div>
  </section>

  <div class="standalone-brand">
    <span class="line-1">Pine Ridge</span>
    <span class="line-2">Canine Coaching</span>
  </div>

</main>
</body>
</html>
```